Business Card Design

I am a realtor and i also flip houses. I am CEO and Founder of my business which is Vantrell Group LLC which is named after my great uncle who died and i was really close to. He was a wonderful friendly man so i want my business to represent him too. My business works with a lot of different people but i want mainly something to show i am a strong confidant woman who owns there own business. I have a really fun personality so i don't want anything TOO serious or manly. I want the perfect mix. My last two business cards i created are too embarrassing to hand out because they are far too girly and i deal with a lot of millionaire clients. I live out in the Palm Springs California area. I think its very important to show i am a single mom, female with her own business at only 24. I don't want to just be a female that blends in with all of the other serious people but yet i don't want to seem immature. People are telling me to stay away from pinks and purples but i don't want blues and greens because they represent men more. But i won't say no to them if there is a happy medium.

Industry/Entity Type

Realtor

Contact Information for Business Card

Vantrell Group, LLC
Corinne Haskett
27385 Sandvale Ave, C2 518
Palm Verde, CA 92284
760-413-6657
Corinnethaskett@mailvern.com

```html
<!DOCTYPE html>
<html lang="en">
<head>
<meta charset="utf-8">
<title>Vantrell Group LLC – Business Card</title>
<link rel="stylesheet" href="https://fonts.googleapis.com/css2?family=Source+Sans+3:wght@400;600&display=swap">
<style>
  :root {
    --page-bg: #e9e7e4;
    --card-black: #050505;
    --circle-red: #e03a22;
    --circle-rim: #fbe3dc;
    --ink-dark: #0b0b0b;
    --ink-light: #ffffff;
    --icon-stroke: #2a1a16;
  }
  * { margin: 0; padding: 0; box-sizing: border-box; }
  html, body {
    width: 1200px; height: 1000px; overflow: hidden;
    background: var(--page-bg);
    font-family: "Source Sans 3", "Myriad Pro", Arial, sans-serif;
  }
  .business-card {
    position: absolute; left: 75px; top: 200px;
    width: 1050px; height: 600px;
    background: var(--card-black);
    overflow: hidden;
    box-shadow: 0 12px 30px rgba(0,0,0,.25);
  }
  .feature-circle {
    position: absolute;
    left: 290px; top: -30px;
    width: 660px; height: 660px;
    border-radius: 50%;
    background: var(--circle-red);
    border: 5px solid var(--circle-rim);
  }
  .brand {
    position: absolute; left: 400px; top: 62px;
    color: var(--ink-dark);
    font-weight: 400; letter-spacing: -2px;
    line-height: 1;
  }
  .brand-name { font-size: 66px; display: block; }
  .brand-suffix {
    display: block; text-align: right;
    font-size: 30px; letter-spacing: 0; margin-top: -4px;
  }
  .holder {
    position: absolute; left: 470px; top: 175px;
    color: var(--ink-dark); text-align: center;
  }
  .holder-name { font-size: 46px; font-weight: 400; line-height: 1; }
  .holder-title { font-size: 24px; font-weight: 400; margin-top: 2px; }
  .contact-list {
    position: absolute; left: 420px; top: 272px;
    list-style: none; color: var(--ink-light);
    font-size: 31px; line-height: 40px;
  }
  .contact-item { display: flex; align-items: flex-start; margin-bottom: 4px; }
  .contact-icon { width: 34px; height: 40px; margin-right: 18px; flex: none; }
  .contact-icon svg { width: 34px; height: 40px; fill: none; stroke: var(--icon-stroke); stroke-width: 1.6; }
</style>
</head>
<body>
  <article class="business-card">
    <div class="feature-circle"></div>

    <div class="brand">
      <span class="brand-name">Vantrell Group</span>
      <span class="brand-suffix">LLC</span>
    </div>

    <div class="holder">
      <h1 class="holder-name">Corinne Haskett</h1>
      <p class="holder-title">CEO and Founder</p>
    </div>

    <ul class="contact-list">
      <li class="contact-item">
        <span class="contact-icon">
          <svg viewBox="0 0 34 40" aria-hidden="true">
            <rect x="10" y="6" width="15" height="28" rx="2.5"/>
            <line x1="10" y1="10" x2="25" y2="10"/>
            <line x1="10" y1="29" x2="25" y2="29"/>
          </svg>
        </span>
        <span>760-413-6657</span>
      </li>
      <li class="contact-item">
        <span class="contact-icon">
          <svg viewBox="0 0 34 40" aria-hidden="true">
            <path d="M17 35 C10 25 7 20 7 15 A10 10 0 0 1 27 15 C27 20 24 25 17 35 Z"/>
            <circle cx="17" cy="15" r="3.5"/>
          </svg>
        </span>
        <span>27385 Sandvale Ave<br>C2 518 Palm Verde<br>CA 92284</span>
      </li>
      <li class="contact-item">
        <span class="contact-icon">
          <svg viewBox="0 0 34 40" aria-hidden="true">
            <rect x="4" y="11" width="26" height="18"/>
            <polyline points="4,11 17,22 30,11"/>
          </svg>
        </span>
        <span>Corinnethaskett@mailvern.com</span>
      </li>
    </ul>
  </article>
</body>
</html>
```